Design a 4-page brochure for Bramble Peak Fund

Please use the content from the Updated Brochure attachment to design a 4-page 4-color glossy letter sized brochure for Bramble Peak Fund. The content and concept of the brochure are in the attached word document. Additional photos are attached, and a logo for the fund will be forthcoming (the logo is currently a contest on ArtworkHive)
We own the attached photos that can be used in brochure.

Target Market(s)

Investors

Industry/Entity Type

Investment

```html
<!DOCTYPE html>
<html lang="en">
<head>
<meta charset="utf-8">
<title>Founding Members – Bramble Peak Fund</title>
<link href="https://fonts.googleapis.com/css2?family=Oswald:wght@700&family=Arimo:wght@400&display=swap" rel="stylesheet">
<style>
  :root{
    --blue:#3aa9e0;
    --dark:#333436;
    --paper:#e7e8ea;
    --ink:#1f1f1f;
    --white:#ffffff;
  }
  html,body{margin:0;padding:0;overflow:hidden;background:var(--paper);}
  .page{position:relative;width:848px;height:1200px;overflow:hidden;background:var(--paper);}
  .top-band-blue{position:absolute;left:0;top:0;width:420px;height:24px;background:var(--blue);clip-path:polygon(0 0,100% 0,95% 100%,0 100%);}
  .top-band-dark{position:absolute;left:400px;top:0;width:448px;height:24px;background:var(--dark);clip-path:polygon(5% 0,100% 0,100% 100%,0 100%);}
  .page-title{position:absolute;left:55px;top:30px;margin:0;font-family:'Oswald',sans-serif;font-weight:700;font-size:51px;line-height:56px;color:var(--blue);letter-spacing:0.3px;white-space:nowrap;transform:scaleX(0.8);transform-origin:left center;}
  .title-rule{position:absolute;left:58px;top:82px;width:790px;height:12px;background:var(--dark);clip-path:polygon(1.5% 0,100% 0,100% 100%,0 100%);}
  .bios{position:absolute;left:28px;top:99px;width:778px;font-family:'Arimo',Arial,sans-serif;font-size:15.8px;line-height:20.7px;color:var(--ink);text-align:justify;}
  .bios p{margin:0 0 20.7px 0;}
  .bios p.gap-lg{margin-bottom:40px;}
  .portrait{width:318px;height:318px;shape-outside:circle(50%);shape-margin:14px;}
  .portrait svg{display:block;width:318px;height:318px;}
  .portrait-one{float:right;margin-right:-42px;}
  .portrait-two{float:left;clear:left;margin-left:-20px;}
  .portrait-three{float:right;clear:right;margin-right:-26px;}
  .spacer-left{float:left;width:1px;height:300px;}
  .spacer-right{float:right;clear:right;width:1px;height:365px;}
  .footer-bar{position:absolute;left:0;bottom:0;width:848px;height:26px;background:var(--dark);}
  .footer-tab{position:absolute;right:0;bottom:0;width:430px;height:26px;background:var(--blue);clip-path:polygon(4% 0,100% 0,100% 100%,0 100%);
    font-family:'Arimo',Arial,sans-serif;font-size:14px;line-height:26px;color:var(--white);text-align:center;}
</style>
</head>
<body>
<div class="page">
  <div class="top-band-blue"></div>
  <div class="top-band-dark"></div>
  <h1 class="page-title">FOUNDING MEMBERS OF BRAMBLE PEAK</h1>
  <div class="title-rule"></div>

  <div class="bios">
    <div class="portrait portrait-one">
      <svg viewBox="0 0 318 318">
        <defs>
          <radialGradient id="tone-one" cx="50%" cy="45%" r="60%">
            <stop offset="0" stop-color="#c9b9a6"/><stop offset="1" stop-color="#6f7d69"/>
          </radialGradient>
        </defs>
        <circle cx="159" cy="159" r="152" fill="none" stroke="var(--dark)" stroke-width="12" stroke-dasharray="90 14"/>
        <circle cx="159" cy="159" r="152" fill="none" stroke="var(--blue)" stroke-width="12" stroke-dasharray="40 150" stroke-dashoffset="20"/>
        <circle cx="159" cy="159" r="140" fill="url(#tone-one)" role="img" aria-label="Portrait photo of Mr. Halvorsen in a navy suit outdoors"/>
      </svg>
    </div>
    <div class="spacer-left"></div>
    <div class="portrait portrait-two">
      <svg viewBox="0 0 318 318">
        <defs>
          <radialGradient id="tone-two" cx="50%" cy="45%" r="60%">
            <stop offset="0" stop-color="#d39a78"/><stop offset="1" stop-color="#5b4838"/>
          </radialGradient>
        </defs>
        <circle cx="159" cy="159" r="152" fill="none" stroke="var(--dark)" stroke-width="12" stroke-dasharray="90 14"/>
        <circle cx="159" cy="159" r="152" fill="none" stroke="var(--blue)" stroke-width="12" stroke-dasharray="45 130" stroke-dashoffset="60"/>
        <circle cx="159" cy="159" r="140" fill="url(#tone-two)" role="img" aria-label="Portrait photo of Mr. Corrigan smiling outdoors"/>
      </svg>
    </div>
    <div class="spacer-right"></div>
    <div class="portrait portrait-three">
      <svg viewBox="0 0 318 318">
        <defs>
          <radialGradient id="tone-three" cx="50%" cy="45%" r="60%">
            <stop offset="0" stop-color="#d8c3ae"/><stop offset="1" stop-color="#4a4d55"/>
          </radialGradient>
        </defs>
        <circle cx="159" cy="159" r="152" fill="none" stroke="var(--dark)" stroke-width="12" stroke-dasharray="90 14"/>
        <circle cx="159" cy="159" r="152" fill="none" stroke="var(--blue)" stroke-width="12" stroke-dasharray="42 140" stroke-dashoffset="100"/>
        <circle cx="159" cy="159" r="140" fill="url(#tone-three)" role="img" aria-label="Portrait photo of Mr. Ashdown in a suit and tie"/>
      </svg>
    </div>

    <p>Mr. Halvorsen is a seasoned CFO and veteran of the financial community with more than thirty years of experience in pioneering new financial vehicles and structures. Early in his career he helped pioneer the NHMA, FLHB, and GHLA pass-through and electronic delivery system. Mr. Halvorsen subsequently turned to securitizing mortgages, where he successfully structured four REMIC security offerings as the CFO of a life insurance company, and was among the first in the nation to use the newly legislated REMIC pass-through structure.</p>
    <p class="gap-lg">Later, Mr. Halvorsen assisted Mr. Ashdown’s firm in structuring the nation’s first mixed mortgage pool, overseeing both loan origination and underwriting, and well as providing the modeling necessary to verify the viability of the pool’s cash flows to achieve investment grade ratings. Mr. Halvorsen managed the team that structured the financing for South Africa’s Redevelopment Program.</p>
    <p>Mr. Corrigan brings over twenty years of entrepreneurial experience to the Fund. He has a background in implementing strategic plans to drive enterprise value, with an emphasis on sales management and business development. Mr. Corrigan has been a co-founder in a number of early stage companies, raising over thirty million dollars in angel financing.</p>
    <p class="gap-lg">At Dentavia Mr. Corrigan chaired the Sales Advisory Council and helped Meridian Care write the IDET procedure into policy. He was a senior sales representative at Surgilane, and winner of the Pinnacle Award and Surgilane Sale Representative of the Year. Mr. Corrigan was responsible for sales at Corvell Medical and financial research and support at Pemberly and Company. He started his career as a pricing analyst at Stratacore, and won a national championship in rowing at Lakeshore State University.</p>
    <p>Mr. Ashdown is a founder of companies in numerous markets, including citrus, finance, education, publishing, and technology. He is a pioneer in structured finance, originating the first commercial mortgage conduit pool in the nation and securing a one billion dollar line of credit from Northgate Capital. He founded a firm that helped structure the financing for the national Redevelopment Program, which provided housing for thousands of families.</p>
    <p>Mr. Ashdown founded Youngstar Magazine, leading its expansion in the US and abroad. The publication was circulated in more than thirty countries, with a readership in the millions. Mr. Ashdown is a co-founder of three technology companies and two charter schools in Colorado; Ridgeline Middle School and Crestview K-12 School, the later of which is consistently ranked in the top fifty schools in the nation by both Weekly Review and National School Report.</p>
  </div>

  <div class="footer-bar"></div>
  <div class="footer-tab">© 2016 Bramble Peak Fund</div>
</div>
</body>
</html>
```